New Payments Start-up requires Logo, Style Guide and Web Site Design

We need a logo, style guide (colour templates etc.) and marketing web-site (HTML/CSS styling) for Brixu, a new account-to-account payment product for use in the Single European Payment Area (SEPA).

The design is for the product only, not a company brand. We're looking for basic palette and style guidelines also. The web site need only be a basic responsive cross-platform design and layout. We will produce our own content.

We have no requirements for specific colours or logo styles. It is a financial product, however, so should not appear too quirky or untrustworthy.

The product is still in the early phases of development, so we're not able to provide pictures or other content.

As a little more detail on how things work, though, our end customers will arrive at our site through redirection from our merchant partners (a number of whom are large multi-national companies) who have offered our services as an alternative to credit card payments. They will be able to set up a SEPA direct debit mandate online in just a few pages, secure that with a password and use it to pay both immediately and in future with a simple confirmation of the password… a quick, easy checkout.

Because we work with large customer in the payments space, whilst we’d like the brand to be modern and appealing, it has to engender trust and stability. Whilst this product is new and in start-up phase, our company has been in alternative payments for nearly 10 years and have strong products in Europe in the Pre-Paid Zent/KelvaPort and Voucher space. We'd like to treat this separately, however, which is why we've briefed accordingly.
Updates

Reason: Apologies for the extension, but I had a couple of designers contact me to say they had completed work but were unable to submit because time ran out. I'll only extend this once, though, because we need to get cracking on the project. Many thanks Tev

Target Market(s)

European alternative payment customers

Industry/Entity Type

Financial

Logo Text

brixu

Coding

Coded - Design and coding required

Number of Pages Required

1 page

Font styles to use
Sans Serif

```html
<!DOCTYPE html>
<html lang="en">
<head>
<meta charset="utf-8">
<title>Brixu – Account-to-Account Payments</title>
<link rel="stylesheet" href="https://fonts.googleapis.com/css2?family=Open+Sans:wght@400;600&family=Roboto+Condensed:wght@400;700&family=Roboto:wght@300;400;500&display=swap">
<style>
  :root {
    --orange: #f26a10;
    --orange-panel: #e8841f;
    --slate: #5f6266;
    --slate-dark: #4f5356;
    --ink: #333333;
    --muted: #555555;
    --light: #f7f7f7;
    --line: #dddddd;
    --white: #ffffff;
    --red: #d9363e;
    --blue-rule: #4a9bd0;
  }
  * { box-sizing: border-box; margin: 0; padding: 0; }
  html, body { width: 1200px; height: 2299px; overflow: hidden; }
  body { position: relative; background: var(--white); font-family: "Open Sans", Arial, sans-serif; color: var(--ink); }
  a { color: inherit; text-decoration: none; }

  /* Header */
  .site-header { position: absolute; top: 0; left: 0; width: 1200px; height: 95px; background: var(--white); box-shadow: 0 1px 3px rgba(0,0,0,.08); z-index: 2; }
  .brand { position: absolute; left: 98px; top: 14px; }
  .brand-name { font-family: "Roboto Condensed", Arial, sans-serif; font-weight: 700; font-size: 48px; line-height: 46px; color: var(--orange); letter-spacing: -1px; }
  .brand-tag { font-family: "Roboto", Arial, sans-serif; font-size: 13px; color: var(--ink); letter-spacing: .5px; margin-left: 8px; }
  .main-nav { position: absolute; top: 40px; left: 416px; display: flex; gap: 33px; font-family: "Roboto", Arial, sans-serif; font-size: 13px; color: #666; letter-spacing: .3px; }
  .btn-signup { position: absolute; left: 930px; top: 34px; width: 82px; height: 29px; background: var(--orange); color: var(--white); font: 500 12px/29px "Roboto", Arial, sans-serif; text-align: center; border-radius: 2px; }
  .btn-login { position: absolute; left: 1022px; top: 34px; width: 80px; height: 29px; border: 1px solid var(--red); color: var(--red); font: 500 12px/27px "Roboto", Arial, sans-serif; text-align: center; border-radius: 2px; }

  /* Hero */
  .hero { position: absolute; top: 95px; left: 0; width: 1200px; height: 568px; }
  .hero-photo { position: absolute; inset: 0; background: linear-gradient(100deg, #e6e2dc 0%, #d8d2c8 30%, #c7cdd6 55%, #a9b8cc 70%, #e3ded6 100%); }
  .hero-copy { position: absolute; left: 97px; top: 110px; }
  .hero-brand { font-family: "Roboto Condensed", Arial, sans-serif; font-weight: 700; font-size: 56px; line-height: 56px; color: var(--orange); letter-spacing: -1px; }
  .hero-title { font-family: "Roboto Condensed", Arial, sans-serif; font-weight: 700; font-size: 24px; color: #333; margin-top: 16px; }
  .hero-text { font-family: "Open Sans", Arial, sans-serif; font-size: 14px; line-height: 21px; color: #333; width: 400px; margin-top: 6px; }
  .slider-arrow { position: absolute; top: 278px; width: 34px; height: 34px; border-radius: 50%; background: rgba(110,110,110,.7); }
  .slider-arrow svg { display: block; margin: 10px auto; }
  .arrow-prev { left: 24px; }
  .arrow-next { left: 1130px; }

  /* Welcome */
  .welcome { position: absolute; top: 663px; left: 0; width: 1200px; height: 440px; background: var(--white); }
  .welcome-art { position: absolute; left: 130px; top: 57px; width: 290px; height: 320px; border-radius: 50%; background: radial-gradient(circle, #f2f2f2 0%, #e4e4e4 60%, #ffffff 72%); }
  .welcome-copy { position: absolute; left: 503px; top: 72px; width: 580px; }
  .welcome-title { font-family: "Roboto Condensed", Arial, sans-serif; font-weight: 400; font-size: 46px; line-height: 56px; color: #3a3a3a; }
  .welcome-title .accent { color: var(--orange); font-weight: 700; }
  .welcome-text { font-size: 12px; line-height: 24px; color: var(--muted); margin-top: 10px; }
  .check-grid { display: grid; grid-template-columns: 283px 283px; row-gap: 14px; margin-top: 22px; list-style: none; font-size: 13px; color: #444; }
  .check-grid li, .check-list li { display: flex; align-items: center; gap: 12px; }
  .btn-read { position: absolute; left: 503px; top: 339px; width: 125px; height: 37px; background: var(--orange); color: var(--white); font: 500 13px/37px "Roboto", Arial, sans-serif; text-align: center; border-radius: 2px; }

  /* Feature panels */
  .features { position: absolute; top: 1103px; left: 0; width: 1200px; height: 410px; display: flex; }
  .feature { position: relative; width: 600px; height: 410px; color: var(--white); padding: 94px 0 0 97px; }
  .feature-accounts { background: linear-gradient(135deg, #6a6d70 0%, var(--slate) 50%, var(--slate-dark) 100%); }
  .feature-anyone { background: linear-gradient(135deg, #ef9230 0%, var(--orange-panel) 55%, #e07812 100%); padding-left: 60px; }
  .feature-title { font-family: "Roboto Condensed", Arial, sans-serif; font-weight: 400; font-size: 30px; line-height: 36px; }
  .feature-text { font-size: 11px; line-height: 19px; width: 430px; margin-top: 8px; }
  .check-list { list-style: none; margin-top: 18px; font-size: 13px; }
  .check-list li { margin-bottom: 12px; }

  /* How it works */
  .how { position: absolute; top: 1513px; left: 0; width: 1200px; height: 540px; background: var(--light); }
  .how-title { position: absolute; top: 40px; width: 1200px; text-align: center; font-family: "Roboto", Arial, sans-serif; font-weight: 400; font-size: 38px; color: #444; }
  .how-rule { position: absolute; top: 103px; left: 563px; width: 74px; height: 2px; background: var(--blue-rule); }
  .step { position: absolute; top: 150px; width: 320px; text-align: center; }
  .step-photo { width: 166px; height: 166px; margin: 0 auto; border-radius: 50%; border: 5px solid var(--white); box-shadow: 0 0 0 1px #ddd; }
  .step-title { font-family: "Roboto", Arial, sans-serif; font-weight: 300; font-size: 20px; color: #333; margin-top: 20px; }
  .step-text { font-size: 11.5px; line-height: 20px; color: var(--muted); width: 280px; margin: 8px auto 0; }
  .btn-outline { display: inline-flex; align-items: center; gap: 6px; margin-top: 14px; height: 32px; padding: 0 18px; border: 1px solid #777; border-radius: 3px; font: 400 12px/30px "Roboto", Arial, sans-serif; color: #444; }
  .step-1 { left: 103px; }
  .step-2 { left: 452px; }
  .step-3 { left: 769px; }
  .photo-1 { background: linear-gradient(135deg, #c8d2dc, #8e9aa8); }
  .photo-2 { background: linear-gradient(135deg, #d46a4a, #e8c7b0 60%, #9aa0a8); }
  .photo-3 { background: linear-gradient(135deg, #e9eef3, #a7b6c6 60%, #5d6b78); }

  /* Subscribe */
  .subscribe { position: absolute; top: 2053px; left: 0; width: 1200px; height: 100px; background: #5b5b5b; }
  .subscribe-mark { position: absolute; left: 80px; top: 18px; }
  .subscribe-plane { position: absolute; left: 198px; top: 34px; }
  .subscribe-text { position: absolute; left: 253px; top: 29px; font-family: "Roboto", Arial, sans-serif; font-size: 15px; line-height: 22px; color: var(--white); letter-spacing: .3px; }
  .subscribe-form { position: absolute; left: 569px; top: 30px; width: 500px; height: 42px; display: flex; }
  .subscribe-input { flex: 1; background: var(--white); border-radius: 21px 0 0 21px; font-size: 12px; color: #555; line-height: 42px; padding-left: 22px; }
  .subscribe-button { width: 127px; background: var(--orange); color: var(--white); border-radius: 0 21px 21px 0; font: 400 13px/42px "Roboto", Arial, sans-serif; text-align: center; }

  /* Footer */
  .site-footer { position: absolute; top: 2153px; left: 0; width: 1200px; height: 146px; background: var(--white); text-align: center; }
  .social { display: flex; justify-content: center; gap: 9px; margin-top: 37px; }
  .social span { width: 27px; height: 27px; border-radius: 50%; background: #777; }
  .footer-nav { margin-top: 16px; font-family: "Roboto", Arial, sans-serif; font-size: 11px; color: #333; letter-spacing: .3px; }
  .footer-nav span.sep { margin: 0 9px; }
  .copyright { margin-top: 8px; font-size: 11px; color: #333; }
</style>
</head>
<body>

<header class="site-header">
  <div class="brand">
    <div class="brand-name">Brixu</div>
    <div class="brand-tag">Payment Startup</div>
  </div>
  <nav class="main-nav">
    <a href="#">ABOUT</a><a href="#">CHECKING</a><a href="#">SAVINGS</a><a href="#">LOANS</a><a href="#">EBANKING</a><a href="#">CONTACT</a>
  </nav>
  <a class="btn-signup" href="#">SIGN UP</a>
  <a class="btn-login" href="#">LOGIN</a>
</header>

<section class="hero">
  <div class="hero-photo" role="img" aria-label="Man in a checked shirt working on a laptop at home with bills on the table"></div>
  <div class="hero-copy">
    <div class="hero-brand">Brixu</div>
    <h1 class="hero-title">ACCOUNT-TO-ACCOUNT PAYMENTS</h1>
    <p class="hero-text">Lorem ipsum dolor sit amet, consectetur adipiscing sed do eiusmod tempor incididunt ut labore et</p>
  </div>
  <span class="slider-arrow arrow-prev"><svg width="14" height="14" viewBox="0 0 14 14"><path d="M9 2 L4 7 L9 12" fill="none" stroke="#fff" stroke-width="2"/></svg></span>
  <span class="slider-arrow arrow-next"><svg width="14" height="14" viewBox="0 0 14 14"><path d="M5 2 L10 7 L5 12" fill="none" stroke="#fff" stroke-width="2"/></svg></span>
</section>

<section class="welcome">
  <div class="welcome-art" role="img" aria-label="Illustration of online payments: laptop with shopping cart surrounded by parcels, gift, card and basket"></div>
  <div class="welcome-copy">
    <h2 class="welcome-title">Welcome to <span class="accent">Brixu</span></h2>
    <p class="welcome-text">Nemo enim ipsam voluptatem quia voluptas sit aspernatur aut odit aut fugit, sed quia consequuntur magni dolores eos qui ratione voluptatem sequi nesciunt. Neque porro quisquam est, qui dolorem ipsum quia dolor sit amet, consectetur, adipisci velit, sed quia non numquam eius modi tempora incidunt ut labore et dolore magnam aliquam quaerat voluptatem.</p>
    <ul class="check-grid">
      <li><svg width="11" height="9" viewBox="0 0 11 9"><path d="M1 4.5 L4 7.5 L10 1" fill="none" stroke="#444" stroke-width="2"/></svg>Log in to Clearline Online® banking</li>
      <li><svg width="11" height="9" viewBox="0 0 11 9"><path d="M1 4.5 L4 7.5 L10 1" fill="none" stroke="#444" stroke-width="2"/></svg>Select the Acct-to-Acct sub tab</li>
      <li><svg width="11" height="9" viewBox="0 0 11 9"><path d="M1 4.5 L4 7.5 L10 1" fill="none" stroke="#444" stroke-width="2"/></svg>Select the Payments tab</li>
      <li><svg width="11" height="9" viewBox="0 0 11 9"><path d="M1 4.5 L4 7.5 L10 1" fill="none" stroke="#444" stroke-width="2"/></svg>Follow instructions on the screen</li>
    </ul>
  </div>
  <a class="btn-read" href="#">READ MORE</a>
</section>

<section class="features">
  <div class="feature feature-accounts" role="img" aria-label="Dim photo of a desk with keyboard, plant and a phone showing a completed transaction">
    <h3 class="feature-title">MOVE MONEY BETWEEN ACCOUNTS</h3>
    <p class="feature-text">Lorem ipsum dolor sit amet, consectetur adipiscing elit, sed do eiusmod tempor incididunt ut labore et dolore magna aliqua. Ut enim ad minim veniam, quis nostrud exercitation ullamco laboris nisi ut aliquip</p>
    <ul class="check-list">
      <li><svg width="11" height="9" viewBox="0 0 11 9"><path d="M1 4.5 L4 7.5 L10 1" fill="none" stroke="#fff" stroke-width="2"/></svg>Log in to Clearline Online® banking</li>
      <li><svg width="11" height="9" viewBox="0 0 11 9"><path d="M1 4.5 L4 7.5 L10 1" fill="none" stroke="#fff" stroke-width="2"/></svg>Select the Payments tab</li>
      <li><svg width="11" height="9" viewBox="0 0 11 9"><path d="M1 4.5 L4 7.5 L10 1" fill="none" stroke="#fff" stroke-width="2"/></svg>Select the Acct-to-Acct sub tab</li>
      <li><svg width="11" height="9" viewBox="0 0 11 9"><path d="M1 4.5 L4 7.5 L10 1" fill="none" stroke="#fff" stroke-width="2"/></svg>Follow instructions on the screen</li>
    </ul>
  </div>
  <div class="feature feature-anyone" role="img" aria-label="Orange-tinted photo of a person paying with a phone">
    <h3 class="feature-title">SEND MONEY TO ANYONE</h3>
    <p class="feature-text">Lorem ipsum dolor sit amet, consectetur adipiscing elit, sed do eiusmod tempor incididunt ut labore et dolore magna aliqua. Ut enim ad minim veniam, quis nostrud exercitation ullamco laboris nisi ut aliquip</p>
    <ul class="check-list">
      <li><svg width="11" height="9" viewBox="0 0 11 9"><path d="M1 4.5 L4 7.5 L10 1" fill="none" stroke="#fff" stroke-width="2"/></svg>Send money to your child at college</li>
      <li><svg width="11" height="9" viewBox="0 0 11 9"><path d="M1 4.5 L4 7.5 L10 1" fill="none" stroke="#fff" stroke-width="2"/></svg>Send a gift to family and friends</li>
      <li><svg width="11" height="9" viewBox="0 0 11 9"><path d="M1 4.5 L4 7.5 L10 1" fill="none" stroke="#fff" stroke-width="2"/></svg>Reimburse friends after a fun night out</li>
      <li><svg width="11" height="9" viewBox="0 0 11 9"><path d="M1 4.5 L4 7.5 L10 1" fill="none" stroke="#fff" stroke-width="2"/></svg>Pay rent to your landlord or roommates</li>
    </ul>
  </div>
</section>

<section class="how">
  <h2 class="how-title">How It Works</h2>
  <div class="how-rule"></div>
  <div class="step step-1">
    <div class="step-photo photo-1" role="img" aria-label="Hands holding a phone next to a laptop"></div>
    <h4 class="step-title">Confirmation of the password</h4>
    <p class="step-text">Lorem ipsum dolor sit amet, consectetur adipiscing elit, sed do eiusmod tempor incididunt ut labore et dolore magna aliqua.</p>
    <a class="btn-outline" href="#">READ MORE <svg width="12" height="8" viewBox="0 0 12 8"><path d="M0 4 H9 M6 1 L10 4 L6 7" fill="none" stroke="#444" stroke-width="1.6"/></svg></a>
  </div>
  <div class="step step-2">
    <div class="step-photo photo-2" role="img" aria-label="Hand holding a payment card over a laptop keyboard"></div>
    <h4 class="step-title">A Quick payment</h4>
    <p class="step-text">Lorem ipsum dolor sit amet, consectetur adipiscing elit, sed do eiusmod tempor incididunt ut labore et dolore magna aliqua.</p>
    <a class="btn-outline" href="#">READ MORE <svg width="12" height="8" viewBox="0 0 12 8"><path d="M0 4 H9 M6 1 L10 4 L6 7" fill="none" stroke="#444" stroke-width="1.6"/></svg></a>
  </div>
  <div class="step step-3">
    <div class="step-photo photo-3" role="img" aria-label="Laptop screen showing a log in form"></div>
    <h4 class="step-title">Easy Checkout</h4>
    <p class="step-text">Lorem ipsum dolor sit amet, consectetur adipiscing elit, sed do eiusmod tempor incididunt ut labore et dolore magna aliqua.</p>
    <a class="btn-outline" href="#">READ MORE <svg width="12" height="8" viewBox="0 0 12 8"><path d="M0 4 H9 M6 1 L10 4 L6 7" fill="none" stroke="#444" stroke-width="1.6"/></svg></a>
  </div>
</section>

<section class="subscribe">
  <svg class="subscribe-mark" width="100" height="70" viewBox="0 0 100 70"><g transform="rotate(-12 50 35)" fill="none" stroke="#6e6e6e" stroke-width="3"><rect x="12" y="12" width="76" height="48" rx="4"/><path d="M12 14 L50 42 L88 14"/></g></svg>
  <svg class="subscribe-plane" width="38" height="34" viewBox="0 0 38 34"><path d="M2 16 L36 2 L28 32 L18 22 Z M18 22 L36 2 M18 22 L17 31 L22 26" fill="none" stroke="#fff" stroke-width="2.2" stroke-linejoin="round"/></svg>
  <p class="subscribe-text">SUBSCRIBE TO RECEIVE UPDATES AND<br>EXCLUSIVE OFFERS.</p>
  <div class="subscribe-form">
    <span class="subscribe-input">Enter your E - mail</span>
    <span class="subscribe-button">SUBSCRIBE</span>
  </div>
</section>

<footer class="site-footer">
  <div class="social"><span></span><span></span><span></span><span></span><span></span></div>
  <div class="footer-nav">HOME<span class="sep">/</span>EBANKING<span class="sep">/</span>LOANS<span class="sep">/</span>SAVINGS<span class="sep">/</span>CHECKING<span class="sep">/</span>COMMUNITY<span class="sep">/</span>CONTACT US</div>
  <p class="copyright">2016 © Copyrights Brixu.All Rights Reserved</p>
</footer>

</body>
</html>
```